Kelvo Tech Oz Business card revamp

We are looking to revamp our business card design. We are hoping to change our colours to dark navey blue, gray, white and black but are open to keeping the same if a good design is submited. We are after somthing a bit differnt not just boring business card. I have attached a copy of our current card. We Want to keep the same logo design which i have attached a few to hopfully help you in this process. We are after a design that can be personalized to separate 4 people

Colors
0455a3
ffffff
000000
cbcbcb

Requirements
Must have
• Kelvo Tech Logo, address 3/41 Mallory Court, Wexhill 4218, phone number, Name and position

```html
<!DOCTYPE html>
<html lang="en">
<head>
<meta charset="utf-8">
<title>Kelvo Tech Oz – Business Card</title>
<link rel="stylesheet" href="https://fonts.googleapis.com/css2?family=Open+Sans:wght@400;600;700;800&display=swap">
<style>
  :root {
    --page-bg: #e9e9e9;
    --card-white: #ffffff;
    --brand-blue: #2f80c8;
    --brand-blue-deep: #1f6db5;
    --brand-orange: #f47b20;
    --text-grey: #6d6d6d;
    --text-white: #ffffff;
  }
  * { box-sizing: border-box; margin: 0; padding: 0; }
  html, body {
    width: 1200px; height: 900px; overflow: hidden;
    background: var(--page-bg);
    font-family: "Open Sans", Arial, sans-serif;
  }
  .canvas {
    position: relative; width: 1200px; height: 900px;
    display: flex; flex-direction: column; align-items: center; justify-content: center; gap: 40px;
  }
  .card {
    position: relative; width: 700px; height: 400px; overflow: hidden;
    box-shadow: 0 8px 24px rgba(0,0,0,0.18);
  }

  /* Front */
  .card-front { background: var(--card-white); }
  .front-brand {
    position: absolute; left: 0; right: 0; top: 130px;
    display: flex; align-items: center; justify-content: center; gap: 16px;
  }
  .brand-dot {
    width: 34px; height: 34px; border-radius: 50%; background: var(--brand-orange);
  }
  .brand-name {
    font-weight: 800; font-size: 52px; color: var(--brand-blue); letter-spacing: -0.5px;
  }
  .services {
    position: absolute; left: 0; right: 0; top: 250px; text-align: center;
    color: var(--text-grey); font-size: 17px; line-height: 1.55;
  }
  .services .sep { color: var(--brand-blue); padding: 0 4px; }

  /* Back */
  .card-back {
    background: linear-gradient(135deg, var(--brand-blue) 0%, var(--brand-blue-deep) 100%);
  }
  .back-art { position: absolute; inset: 0; }
  .contact {
    position: absolute; left: 44px; top: 170px; color: var(--text-white);
  }
  .contact-name { font-weight: 700; font-size: 20px; letter-spacing: 0.5px; }
  .contact-role { font-size: 17px; margin-bottom: 22px; }
  .contact-address { font-size: 16px; line-height: 1.4; margin-bottom: 6px; }
  .contact-list { list-style: none; font-size: 16px; line-height: 1.55; }
  .contact-list li { display: flex; align-items: center; gap: 10px; }
  .contact-list svg { width: 14px; height: 14px; fill: var(--text-white); flex: none; }
</style>
</head>
<body>
<main class="canvas">

  <section class="card card-front" aria-label="Card front">
    <div class="front-brand">
      <span class="brand-dot" aria-hidden="true"></span>
      <span class="brand-name">Kelvo Tech</span>
    </div>
    <p class="services">
      Service Fenotrations<span class="sep">•</span>Steel Spray coatings<span class="sep">•</span>Intumescent paint<br>
      Boot Spray &amp; Wrags<span class="sep">•</span>Fire&amp;Savoke Barriers<span class="sep">•</span>Fire Rated Walls Ceilings
    </p>
  </section>

  <section class="card card-back" aria-label="Card back">
    <svg class="back-art" viewBox="0 0 700 400" aria-hidden="true">
      <circle cx="520" cy="150" r="230" fill="var(--card-white)"/>
      <circle cx="520" cy="150" r="230" fill="none" stroke="var(--brand-orange)" stroke-width="10"/>
      <circle cx="540" cy="140" r="26" fill="var(--brand-orange)"/>
    </svg>
    <div class="contact">
      <p class="contact-name">LIAM CARTER</p>
      <p class="contact-role">Director</p>
      <p class="contact-address">3/41 Mallory Court,<br>Wexhill 4218</p>
      <ul class="contact-list">
        <li>
          <svg viewBox="0 0 16 16"><path d="M3 1h3l1.5 4-2 1.5a9 9 0 0 0 4 4l1.5-2 4 1.5v3c0 1-1 2-2 2A13 13 0 0 1 1 3c0-1 1-2 2-2z"/></svg>
          614 902 7315
        </li>
        <li>
          <svg viewBox="0 0 16 16"><path d="M1 3h14v10H1z M2 4l6 5 6-5" fill="none" stroke="#fff" stroke-width="1.5"/></svg>
          name@kelvotech.com.au
        </li>
        <li>
          <svg viewBox="0 0 16 16"><circle cx="8" cy="8" r="6.5" fill="none" stroke="#fff" stroke-width="1.5"/><path d="M1.5 8h13M8 1.5c-3 3.5-3 9.5 0 13M8 1.5c3 3.5 3 9.5 0 13" fill="none" stroke="#fff" stroke-width="1.2"/></svg>
          www.kelvotech.com.au
        </li>
      </ul>
    </div>
  </section>

</main>
</body>
</html>
```